Hello there!
I am looking to have a label created for a jojoba oil product I am launching. I have attached the logo of my company below. The label should have the following information on it as well:
Ingredients: pure jojoba oil
Size of the bottle: 118ml
And there might be more but I am working on this and will keep you posted.

```html
<!DOCTYPE html>
<html lang="en">
<head>
<meta charset="UTF-8">
<title>Meadowlark Hair Atelier – Jojoba Oil Label</title>
<link href="https://fonts.googleapis.com/css2?family=Archivo+Black&family=Cormorant+Garamond:wght@500&family=Montserrat:wght@500;600&display=swap" rel="stylesheet">
<style>
  :root {
    --backdrop: #e4e4e4;
    --leaf-green: #6f9a36;
    --leaf-green-light: #86ad4c;
    --label-white: #f7f8f4;
    --ink-green: #2f3f1c;
    --ink-grey: #5c5f57;
    --art-pale: #e6ecdd;
    --art-mid: #c9d6b6;
  }
  * { margin: 0; padding: 0; box-sizing: border-box; }
  html, body {
    width: 1200px;
    height: 800px;
    overflow: hidden;
    background: var(--backdrop);
  }
  .canvas {
    position: relative;
    width: 1200px;
    height: 800px;
  }
  .label {
    position: absolute;
    left: 368px;
    top: 20px;
    width: 464px;
    height: 760px;
    background: var(--leaf-green);
    overflow: hidden;
  }
  .label__tagline {
    position: absolute;
    left: 26px;
    top: 18px;
    width: 430px;
    font-family: "Montserrat", sans-serif;
    font-weight: 500;
    font-size: 20px;
    letter-spacing: 12px;
    color: var(--label-white);
    white-space: nowrap;
  }
  .label__product {
    position: absolute;
    left: 40px;
    top: 400px;
    transform: translate(-50%, -50%) rotate(-90deg);
    font-family: "Archivo Black", sans-serif;
    font-size: 46px;
    letter-spacing: 8px;
    color: var(--label-white);
    white-space: nowrap;
  }
  .label__panel {
    position: absolute;
    left: 76px;
    top: 62px;
    right: -10px;
    bottom: 0;
    background: var(--label-white);
    border: 8px solid var(--leaf-green-light);
    border-right: none;
    border-bottom: none;
    border-top-left-radius: 42px;
    overflow: hidden;
  }
  .label__art {
    position: absolute;
    left: 0;
    top: 0;
    width: 100%;
    height: 480px;
    background: radial-gradient(ellipse at 55% 45%, var(--art-mid) 0%, var(--art-pale) 55%, var(--label-white) 100%);
  }
  .label__brand {
    position: absolute;
    left: 18px;
    top: 500px;
    width: 360px;
    font-family: "Cormorant Garamond", serif;
    font-weight: 500;
    font-size: 42px;
    line-height: 1.05;
    letter-spacing: 1px;
    color: var(--ink-green);
    text-transform: uppercase;
  }
  .label__rule {
    position: absolute;
    left: 18px;
    height: 1.5px;
    width: 370px;
    background: var(--ink-green);
  }
  .label__rule--upper { top: 600px; }
  .label__rule--lower { top: 610px; }
  .label__volume {
    position: absolute;
    left: 0;
    top: 640px;
    width: 380px;
    text-align: center;
    font-family: "Montserrat", sans-serif;
    font-weight: 600;
    font-size: 28px;
    color: var(--ink-grey);
  }
</style>
</head>
<body>
  <main class="canvas">
    <section class="label">
      <p class="label__tagline">100%&nbsp;&nbsp;PURE&nbsp;&nbsp;OIL</p>
      <h1 class="label__product">JOJOBA OIL</h1>
      <div class="label__panel">
        <div class="label__art" role="img" aria-label="Line-art illustration of a jojoba branch with leaves and seed pods over a faint leaf pattern"></div>
        <p class="label__brand">Meadowlark<br>Hair Atelier</p>
        <div class="label__rule label__rule--upper"></div>
        <div class="label__rule label__rule--lower"></div>
        <p class="label__volume">118 ML</p>
      </div>
    </section>
  </main>
</body>
</html>
```